Business Card Design Project

Company name will be Tallow Crest (named after my black lab and his fraying muzzle) Business is in the body armor, Security product industry servicing the state, local, and federal law enforcement markets. I want a more formal and serious logo for both business cards and letterhead

```html
<!DOCTYPE html>
<html lang="en">
<head>
<meta charset="utf-8">
<title>Tallow Crest – Business Card</title>
<link rel="stylesheet" href="https://fonts.googleapis.com/css2?family=Questrial&display=swap">
<style>
  :root {
    --wall-light: #eeeeee;
    --wall-mid: #d9d9d9;
    --band-dark: #231f20;
    --ink-dark: #1f1c1d;
    --ink-light: #ffffff;
    --tag-bg: #e6e6e6;
    --mark-square: #3b3b3b;
  }
  html, body {
    margin: 0;
    padding: 0;
    overflow: hidden;
    background: #ffffff;
  }
  .card {
    position: relative;
    width: 1200px;
    height: 686px;
    overflow: hidden;
    font-family: "Questrial", sans-serif;
  }
  .wall {
    position: absolute;
    left: 0;
    top: 0;
    width: 1200px;
    height: 442px;
    background: linear-gradient(180deg, var(--wall-light) 0%, var(--wall-mid) 55%, var(--wall-light) 100%);
  }
  .brand-square {
    position: absolute;
    left: 45px;
    top: 75px;
    width: 95px;
    height: 95px;
    background: var(--mark-square);
  }
  .brand-name {
    position: absolute;
    right: 50px;
    top: 62px;
    margin: 0;
    font-size: 100px;
    font-weight: 400;
    line-height: 1.1;
    letter-spacing: 1px;
    color: var(--ink-dark);
    white-space: nowrap;
  }
  .contact-band {
    position: absolute;
    left: 0;
    top: 442px;
    width: 1200px;
    height: 244px;
    background: var(--band-dark);
    color: var(--ink-light);
  }
  .contact-line {
    position: absolute;
    right: 66px;
    display: flex;
    align-items: center;
    gap: 18px;
    font-size: 27px;
    letter-spacing: 0.5px;
    white-space: nowrap;
  }
  .contact-tag {
    display: inline-flex;
    align-items: center;
    justify-content: center;
    width: 24px;
    height: 24px;
    background: var(--tag-bg);
    color: var(--ink-dark);
    font-size: 15px;
  }
  .contact-address { top: 31px; }
  .contact-phone   { top: 100px; }
  .contact-mobile  { top: 134px; }
  .contact-email {
    position: absolute;
    left: 48px;
    top: 134px;
    font-size: 27px;
    letter-spacing: 0.5px;
    line-height: 34px;
  }
</style>
</head>
<body>
  <main class="card">
    <div class="wall" role="img" aria-label="White painted brick wall texture"></div>
    <div class="brand-square" aria-hidden="true"></div>
    <h1 class="brand-name">TALLOW CREST</h1>

    <section class="contact-band">
      <div class="contact-line contact-address">
        <span>27, MARLOW STREET, KTN 406</span>
        <span class="contact-tag">A</span>
      </div>
      <div class="contact-line contact-phone">
        <span>020 381 672 09</span>
        <span class="contact-tag">T</span>
      </div>
      <div class="contact-line contact-mobile">
        <span>07845 6029 317</span>
        <span class="contact-tag">M</span>
      </div>
      <div class="contact-email">INFO@TALLOWCREST.COM</div>
    </section>
  </main>
</body>
</html>
```